Wine label refresh

We are wanting to modify our Corran Estate label to include a picture on it.
I have attached the pictures below which we would like on the label. They are of the Corran Estate vineyard. I have also attached an example of another label with a picture on it that we like the style of.
Industry/Entity Type
Vineyard
Requirements
Must have
- The Corran Estate text must stay the same but can be moved down. It still needs to be the same size though.
Marlborough Sauvignon Blanc should remain in the same font and roughly the same size.
Wine of New Zealand also must stay but could potentially be moved.
Nice to have
- It would be nice if we could keep the KL logo on the front label but feel free to experiment with where this goes.

```html
<!DOCTYPE html>
<html lang="en">
<head>
<meta charset="utf-8">
<title>Corran Estate – Marlborough Sauvignon Blanc label</title>
<link rel="stylesheet" href="https://fonts.googleapis.com/css2?family=Cinzel:wght@400;500&family=La+Belle+Aurore&display=swap">
<style>
  :root {
    --page: #ffffff;
    --wine: #a3195b;
    --gold-light: #f6e7b8;
    --gold-mid: #d8b86a;
    --gold-dark: #a8873a;
    --sky-top: #a9c6e6;
    --sky-low: #eef3f8;
    --haze: #dfe6e0;
    --hill: #9fb38f;
    --hill-dark: #4f6b40;
    --foliage: #24381f;
    --dots: rgba(163, 25, 91, 0.7);
  }
  * { box-sizing: border-box; margin: 0; padding: 0; }
  html, body {
    width: 1200px;
    height: 4235px;
    overflow: hidden;
    background: var(--page);
  }
  .canvas {
    position: relative;
    width: 1200px;
    height: 4235px;
  }
  .label {
    position: absolute;
    left: 104px;
    top: 2052px;
    width: 980px;
    height: 970px;
    overflow: hidden;
  }
  .gold-band {
    position: absolute;
    left: 0;
    width: 100%;
    height: 32px;
    background: linear-gradient(180deg, var(--gold-dark), var(--gold-light) 40%, var(--gold-mid) 70%, var(--gold-dark));
    z-index: 3;
  }
  .gold-band--top { top: 0; }
  .gold-band--bottom { bottom: 0; }
  .vineyard-photo {
    position: absolute;
    inset: 0;
    background:
      linear-gradient(180deg,
        var(--sky-top) 0%,
        var(--sky-low) 38%,
        var(--sky-low) 52%,
        var(--haze) 60%,
        var(--hill) 68%,
        var(--hill-dark) 78%,
        var(--foliage) 100%);
  }
  .label-content {
    position: absolute;
    inset: 0;
    z-index: 2;
    text-align: center;
    color: var(--wine);
  }
  .brand-mark {
    position: absolute;
    top: 160px;
    left: 0;
    width: 100%;
    display: flex;
    justify-content: center;
    align-items: center;
    gap: 16px;
    font-family: "Cinzel", serif;
    font-size: 58px;
    font-weight: 500;
    line-height: 1;
    letter-spacing: 2px;
  }
  .brand-mark__dot {
    width: 18px;
    height: 18px;
    border-radius: 50%;
    background: var(--wine);
  }
  .estate-name {
    position: absolute;
    top: 292px;
    left: 0;
    width: 100%;
    font-family: "Cinzel", serif;
    font-size: 58px;
    font-weight: 500;
    line-height: 1;
    letter-spacing: 2px;
  }
  .rule {
    position: absolute;
    left: 190px;
    width: 600px;
    border-top: 3px dotted var(--dots);
  }
  .rule--upper { top: 374px; }
  .rule--lower { top: 464px; }
  .varietal {
    position: absolute;
    top: 392px;
    left: 0;
    width: 100%;
    font-family: "La Belle Aurore", cursive;
    font-size: 42px;
    line-height: 1.3;
    white-space: nowrap;
  }
  .origin {
    position: absolute;
    top: 580px;
    left: 0;
    width: 100%;
    font-family: "Cinzel", serif;
    font-size: 30px;
    font-weight: 400;
    line-height: 1;
    letter-spacing: 3px;
  }
</style>
</head>
<body>
  <main class="canvas">
    <section class="label">
      <div class="gold-band gold-band--top"></div>
      <div class="vineyard-photo" role="img" aria-label="Photograph of the Corran Estate vineyard: pale sky, green hills, palm trees and a farm building"></div>
      <div class="label-content">
        <div class="brand-mark"><span class="brand-mark__dot"></span><span>KL</span></div>
        <h1 class="estate-name">CORRAN ESTATE</h1>
        <div class="rule rule--upper"></div>
        <p class="varietal">Marlborough Sauvignon Blanc 2012</p>
        <div class="rule rule--lower"></div>
        <p class="origin">WINE OF NEW ZEALAND</p>
      </div>
      <div class="gold-band gold-band--bottom"></div>
    </section>
  </main>
</body>
</html>
```